menu buttom design

We are looking for a menu button design, similar too the one we have posted in the files section.
They must be quite big and prominent on the page. They will be down the right hand side of the website which has a large video player on as well. We would like them to look a little like TV buttons, not not cliched.
The titles on each button are as follows:
Whats new, Buy and sell, Join in, More TV, More Info, more web
The web page will be black.
PLEASE concentrate more on the colours and text that making the buttons different shapes.
It must look classy, sophistocated, beautiful design

Target Market(s)

Web Tv watchers

Requirements
Must have
• Should be similar to what I have uploaded on the file.
Should be rectangular, raised up to give button effect with some shine.
What we would really like to to have some sorts of graphics behind the text to show the various
pages. We would like more subtle, maybe pastel colours that work well together and a really nice font that works well.
Concentrate more on the colours and fonts and the overall look rather than different shapes.
These buttons are for mock up web pages, but when the pages are made we will us the buttons as templates and will animate them when you roll over them.

```html
<!DOCTYPE html>
<html lang="en">
<head>
<meta charset="utf-8">
<title>Menu Buttons</title>
<link href="https://fonts.googleapis.com/css2?family=Jost:wght@400&display=swap" rel="stylesheet">
<style>
  :root {
    --page-bg: #000000;
    --frame-light: #fafafa;
    --frame-mid: #e2e2e2;
    --frame-dark: #b9b9b9;
    --frame-edge: #8f8f8f;
    --label: #ffffff;

    --red-top: #ff7f86;
    --red-upper: #f8434c;
    --red-lower: #e6000c;
    --red-bottom: #ff3a40;
    --red-edge: #a80008;

    --blue-top: #7fd8ff;
    --blue-upper: #28b3ee;
    --blue-lower: #0792d6;
    --blue-bottom: #27b0f0;
    --blue-edge: #045f92;

    --green-top: #8ee77e;
    --green-upper: #4fd23d;
    --green-lower: #16bf05;
    --green-bottom: #3fd62e;
    --green-edge: #0a7a02;

    --amber-top: #ffd775;
    --amber-upper: #ffc233;
    --amber-lower: #ffb600;
    --amber-bottom: #ffc92e;
    --amber-edge: #c98400;

    --orange-top: #ffbf73;
    --orange-upper: #ff9a2e;
    --orange-lower: #ff7f00;
    --orange-bottom: #ff9a2a;
    --orange-edge: #c25800;

    --violet-top: #ea8cf4;
    --violet-upper: #d351e5;
    --violet-lower: #b60ccf;
    --violet-bottom: #d44ae8;
    --violet-edge: #7a0690;
  }

  * { margin: 0; padding: 0; box-sizing: border-box; }

  html, body {
    width: 1200px;
    height: 900px;
    overflow: hidden;
    background: var(--page-bg);
  }

  .menu {
    position: relative;
    width: 1200px;
    height: 900px;
  }

  .menu-button {
    position: absolute;
    width: 260px;
    height: 209px;
    padding: 10px;
    border-radius: 13px;
    background: linear-gradient(180deg, var(--frame-light) 0%, var(--frame-mid) 55%, var(--frame-dark) 100%);
    border: 1px solid var(--frame-edge);
    box-shadow: inset 0 1px 0 #ffffff, inset 0 -2px 3px rgba(0,0,0,0.18);
    text-decoration: none;
  }

  .menu-button .face {
    display: flex;
    flex-direction: column;
    align-items: center;
    justify-content: center;
    width: 100%;
    height: 100%;
    border-radius: 7px;
    border: 1px solid var(--edge);
    background: linear-gradient(180deg,
      var(--top) 0%,
      var(--upper) 49%,
      var(--lower) 51%,
      var(--lower) 62%,
      var(--bottom) 100%);
    box-shadow: inset 0 2px 4px rgba(255,255,255,0.35), inset 0 -3px 6px rgba(255,255,255,0.18);
    font-family: "Jost", "Futura", sans-serif;
    font-weight: 400;
    color: var(--label);
    text-align: center;
    text-transform: uppercase;
    line-height: 1;
  }

  .label-line {
    display: block;
    font-size: 46px;
    letter-spacing: 0.5px;
    margin: 3px 0;
  }

  .label-small {
    display: block;
    font-size: 29px;
    margin: 4px 0;
  }

  .col-left  { left: 265px; }
  .col-right { left: 673px; }
  .row-1 { top: 69px; }
  .row-2 { top: 345px; }
  .row-3 { top: 621px; }

  .tone-red    { --top: var(--red-top);    --upper: var(--red-upper);    --lower: var(--red-lower);    --bottom: var(--red-bottom);    --edge: var(--red-edge); }
  .tone-blue   { --top: var(--blue-top);   --upper: var(--blue-upper);   --lower: var(--blue-lower);   --bottom: var(--blue-bottom);   --edge: var(--blue-edge); }
  .tone-green  { --top: var(--green-top);  --upper: var(--green-upper);  --lower: var(--green-lower);  --bottom: var(--green-bottom);  --edge: var(--green-edge); }
  .tone-amber  { --top: var(--amber-top);  --upper: var(--amber-upper);  --lower: var(--amber-lower);  --bottom: var(--amber-bottom);  --edge: var(--amber-edge); }
  .tone-orange { --top: var(--orange-top); --upper: var(--orange-upper); --lower: var(--orange-lower); --bottom: var(--orange-bottom); --edge: var(--orange-edge); }
  .tone-violet { --top: var(--violet-top); --upper: var(--violet-upper); --lower: var(--violet-lower); --bottom: var(--violet-bottom); --edge: var(--violet-edge); }
</style>
</head>
<body>
  <nav class="menu">
    <a class="menu-button col-left row-1 tone-red" href="#">
      <span class="face"><span class="label-line">Whats</span><span class="label-line">New</span></span>
    </a>
    <a class="menu-button col-right row-1 tone-amber" href="#">
      <span class="face"><span class="label-line">More</span><span class="label-line">TV</span></span>
    </a>
    <a class="menu-button col-left row-2 tone-blue" href="#">
      <span class="face"><span class="label-line">Buy</span><span class="label-small">and</span><span class="label-line">Sell</span></span>
    </a>
    <a class="menu-button col-right row-2 tone-orange" href="#">
      <span class="face"><span class="label-line">More</span><span class="label-line">Info</span></span>
    </a>
    <a class="menu-button col-left row-3 tone-green" href="#">
      <span class="face"><span class="label-line">Join</span><span class="label-line">In</span></span>
    </a>
    <a class="menu-button col-right row-3 tone-violet" href="#">
      <span class="face"><span class="label-line">More</span><span class="label-line">Web</span></span>
    </a>
  </nav>
</body>
</html>
```